Amberline Picture Works Web Design

COMPANY: AMBERLINE PICTURE WORKS
LOCATION: SHANGHAI, CHINA
AREA: FILM/TV DRAMA/COMMERCIALS/GAME POST PRODUCTION, SOUND DESIGN, MUSIC, and GAME.
WEB STYLE: SIMPLE, PROFESSIONAL, TRUSTWORTHY

LANGUAGE: ENGLISH, CHINESE. (Same layout, different language)
UPDATE: AFTER PROJECT FINISHED, WE NEED UPDATE BY OURSELVES.

MAIN SUBJECT: 6
1 HOMEPAGE
2 ABOUT US
3 TEAM
4 SERVICES
5 FACILITY
6 CONTACT

add one page of JOB OPPORTUNITIES.

DETAILS
1 HOMEPAGE
SLOGAN: Amberline Picture Works provides a well-designed working environment which amplifies your team’s ability to reach their creative goals.

Our services include:
 Feature Films
 Music & Scoring
 Commercials
 ADR & Foley
 Sound & Picture Editorial
 Sound Design
 Video Game

2 ABOUT US
Amberline Picture Works is located in the premiere South-Bund area of Shanghai. Occupying a 5000 square meter Technical Building, Amberline Picture Works was built by a filmmaker for filmmakers, and is one of the largest, most versatile full-service post-production facilities in China.

Amberline Picture Works is positioning to be at the forefront of the latest technology. Our goal is to provide a comprehensive solution for the post-production needs of our clients. We offer two fully-equipped dubbing stages (one of which will be certified VORTAN SPHERA ELITE), a large variety of both picture and sound editing rooms, impressive Foley and ADR stages, a world-class scoring stage, and complete audio and video transfer services.

We can handle your entire project from editing all the way to the end of the final sound mix; all under one extremely comfortable roof. We fully realize that the true art is in listening to the needs of our clients and making their greatest vision a reality. To this end our creative team's expertise, with a network of sound supervisors, editors and mixers, will deliver the magic you need. Producers and directors will also find our richly appointed guest accommodations to be a comfortable and soothing place to wind up the day. Every aspect of your project will be taken care of by a skilled and dedicated team, in the way that is best suited to you.

3 TEAM
(attachment 01)

4 SERVICES
Sound Mix
ADR
FOLEY
MUSIC
Sound Design
Sound Edit
Picture Edit
for all the Films, TV Drama, Commercials, Video Games, Online Media
(attachment 02, use photo)

5 FACILITY
(attachment 03)

6 CONTACT
(attachment04)
with map

Reason: Designers work are great, my bosses will spend 1-2 days select one of these web design, and spend 1-2 days to make some change, maybe use new photos.

```html
<!DOCTYPE html>
<html lang="en">
<head>
<meta charset="utf-8">
<title>Amberline Picture Works</title>
<link rel="stylesheet" href="https://fonts.googleapis.com/css2?family=Oswald:wght@500&family=Montserrat:wght@400&display=swap">
<style>
  :root {
    --studio-dark: #1e1a15;
    --studio-warm: #4a3f31;
    --brand-blue: #1f7fc4;
    --brand-blue-soft: rgba(31, 127, 196, 0.55);
    --ink-light: #ffffff;
    --ink-muted: #c9c9c9;
    --badge-dark: #0b0d10;
  }
  * { margin: 0; padding: 0; box-sizing: border-box; }
  html, body { width: 1200px; height: 600px; overflow: hidden; background: var(--studio-dark); }
  .hero {
    position: relative;
    width: 1200px;
    height: 600px;
    overflow: hidden;
    font-family: "Montserrat", sans-serif;
    color: var(--ink-light);
  }
  .hero__photo {
    position: absolute; inset: 0;
    background:
      radial-gradient(ellipse at 70% 35%, #6a5b45 0%, transparent 55%),
      linear-gradient(160deg, var(--studio-warm) 0%, #2c251d 55%, var(--studio-dark) 100%);
  }
  .hero__shapes { position: absolute; inset: 0; }
  .progress {
    position: absolute; top: 10px; left: 1008px; width: 180px; height: 2px;
    background: rgba(255,255,255,0.45);
  }
  .progress__fill { width: 32px; height: 100%; background: var(--brand-blue); }
  .slide-index {
    position: absolute; top: 15px; left: 1027px;
    display: flex; gap: 14px; list-style: none;
    font-size: 10px; color: var(--ink-light);
  }
  .brand-badge {
    position: absolute; left: 184px; top: 232px;
    width: 160px; height: 160px; border-radius: 50%;
    background: var(--badge-dark);
    border: 2px solid #5a5a5a;
    box-shadow: 0 0 0 8px rgba(0,0,0,0.35);
    display: flex; align-items: center; justify-content: center; text-align: center;
  }
  .brand-badge__name {
    font-family: "Oswald", sans-serif; font-weight: 500;
    font-size: 20px; line-height: 1.1; color: var(--brand-blue);
    letter-spacing: 1px;
  }
  .headline {
    position: absolute; left: 428px; top: 222px;
    font-family: "Oswald", sans-serif; font-weight: 500;
    font-size: 31px; line-height: 36px; letter-spacing: -0.2px;
    text-transform: uppercase; color: var(--ink-light);
  }
  .services {
    position: absolute; left: 428px; top: 452px; width: 560px;
    display: flex; flex-wrap: wrap; row-gap: 12px; column-gap: 28px;
    list-style: none; font-size: 11px; letter-spacing: 0.2px;
  }
  .services li::before { content: "+"; font-size: 14px; margin-right: 6px; font-weight: 400; }
  .services__break { flex-basis: 100%; height: 0; }
  .next-arrow { position: absolute; left: 1134px; top: 284px; }
  .pager {
    position: absolute; left: 427px; top: 571px;
    display: flex; gap: 4px; list-style: none;
  }
  .pager li { width: 9px; height: 9px; border-radius: 50%; border: 1px solid var(--ink-muted); }
  .pager li.is-active { background: var(--brand-blue); border-color: var(--brand-blue); }
</style>
</head>
<body>
<section class="hero">
  <div class="hero__photo" role="img" aria-label="Photo of a sound mixing studio with console, touch screen, monitors and an engineer at the desk"></div>

  <svg class="hero__shapes" width="1200" height="600" viewBox="0 0 1200 600" aria-hidden="true">
    <polygon points="0,0 436,0 88,600 0,600" fill="var(--brand-blue-soft)"/>
    <polygon points="0,0 340,0 0,560" fill="rgba(31,127,196,0.35)"/>
    <polygon points="1200,232 1200,600 988,600" fill="var(--brand-blue-soft)"/>
    <polygon points="1200,420 1200,600 1094,600" fill="rgba(31,127,196,0.4)"/>
  </svg>

  <div class="progress"><div class="progress__fill"></div></div>
  <ol class="slide-index">
    <li>01</li><li>02</li><li>03</li><li>04</li><li>05</li><li>06</li>
  </ol>

  <div class="brand-badge"><span class="brand-badge__name">AMBERLINE<br>PICTURE<br>WORKS</span></div>

  <h1 class="headline">Amberline Picture Works<br>provides a well-designed<br>working environment<br>which amplifies your team’s ability<br>to reach their creative goals</h1>

  <ul class="services">
    <li>FEATURE FILMS</li><li>MUSIC &amp; SCORING</li><li>COMMERCIALS</li>
    <li class="services__break"></li>
    <li>ADR &amp; FOLEY</li><li>SOUND &amp; PICTURE EDITORIAL</li><li>SOUND DESIGN</li><li>VIDEO GAME</li>
  </ul>

  <svg class="next-arrow" width="20" height="40" viewBox="0 0 20 40" aria-label="Next slide">
    <polyline points="2,2 18,20 2,38" fill="none" stroke="#cfcfcf" stroke-width="2"/>
  </svg>

  <ul class="pager">
    <li></li><li class="is-active"></li><li></li><li></li><li></li>
  </ul>
</section>
</body>
</html>
```